RKS Rovalin Kestra Sulvane company brochure

We need the design of brochure of a company that provides consultancy, design and supply of key equipment in the field of Wastewater, clean water, organic waste anaerobic treatment and green energy production for Industries. The attached files are:
RKS wording in english that describes activities
Some drawings (useful for design)
Presentation (in italian)
It would be nice to have a 4 pages brochure possibly in double language (english and italian).

Target Market(s)

water and waste

Industry/Entity Type

It Company

Colors

Designer to choose colors to be used in the design.

Requirements
Must have
• use the logo RKS as per attached docs

```html
<!DOCTYPE html>
<html lang="en">
<head>
<meta charset="utf-8">
<title>RKS Rovalin Kestra Sulvane – Biological Oxidative Treatment brochure</title>
<link href="https://fonts.googleapis.com/css2?family=Montserrat:wght@300;400;600;700&family=Questrial&display=swap" rel="stylesheet">
<style>
  :root{
    --stage:#a9a9a9;
    --paper:#ffffff;
    --paper-shade:#e4e7ee;
    --ink:#2b2d33;
    --ink-soft:#4a4d55;
    --orange:#e4541b;
    --orange-dark:#c9400f;
    --blue:#2f5f97;
    --magenta:#c2185b;
    --green:#5a9a2e;
  }
  *{box-sizing:border-box;margin:0;padding:0}
  html,body{width:1200px;height:789px;overflow:hidden;background:var(--stage)}
  body{font-family:"Questrial",sans-serif;color:var(--ink)}
  .spread{position:absolute;left:85px;top:30px;width:1030px;height:729px;display:flex;box-shadow:0 8px 24px rgba(0,0,0,.25)}
  .page{position:relative;width:515px;height:729px;overflow:hidden;background:var(--paper)}

  /* back page */
  .page--back{background:linear-gradient(160deg,#ffffff 0%,#f1f3f7 55%,var(--paper-shade) 100%)}
  .top-band{position:absolute;left:0;top:0;width:100%;height:9px;background:var(--orange)}
  .top-band::after{content:"";position:absolute;left:0;top:9px;width:100%;height:3px;background:var(--orange-dark);opacity:.35}
  .about{position:absolute;left:40px;top:42px;width:440px}
  .section-title{font-family:"Montserrat",sans-serif;font-weight:700;font-size:25px;color:var(--ink)}
  .section-rule{width:140px;height:3px;background:var(--blue);margin:6px 0 14px}
  .about p{font-size:12px;line-height:1.5;color:var(--ink-soft);margin-bottom:8px}
  .block-blue{position:absolute;background:var(--blue)}
  .block-blue--right{left:300px;top:222px;width:215px;height:240px}
  .block-blue--left{left:0;top:310px;width:42px;height:240px}
  .photo{position:absolute;border:5px solid #fff;box-shadow:0 2px 6px rgba(0,0,0,.2)}
  .photo--tank{left:62px;top:256px;width:270px;height:150px;background:linear-gradient(180deg,#cfd6dc 0%,#8fa3a8 45%,#6d9c9a 100%)}
  .photo--plant{left:92px;top:418px;width:270px;height:142px;background:linear-gradient(180deg,#bfc8cc 0%,#7f8f80 45%,#a9aeae 100%)}
  .contact{position:absolute;left:60px;top:578px}
  .contact .section-title{color:var(--magenta);font-size:20px;line-height:1.2}
  .contact .section-rule{width:120px;margin:3px 0 7px}
  .contact-list{list-style:none;font-size:13px;line-height:1.35;color:var(--ink)}
  .contact-list li{display:flex;align-items:flex-start;gap:8px}
  .contact-list svg{flex:none;margin-top:2px}
  .contact-list .indent{padding-left:22px}
  .social{position:absolute;right:22px;bottom:60px;display:flex;gap:6px}
  .social span{width:22px;height:22px;border:1.5px solid var(--blue);border-radius:50%}

  /* front page */
  .front-accent{position:absolute;left:0;top:0;width:125px;height:7px;background:var(--orange)}
  .brand{position:absolute;left:0;top:34px;width:100%;display:flex;justify-content:center;align-items:center;gap:10px}
  .brand-mark{width:16px;height:16px;background:var(--green)}
  .brand-name{font-family:"Montserrat",sans-serif;font-weight:700;font-size:19px;color:var(--green);line-height:1.15}
  .cover-photo{position:absolute;left:0;top:130px;width:515px;height:520px;background:linear-gradient(180deg,#c9ccce 0%,#d1c17f 30%,#b8a664 55%,#6d6a5a 80%,#4a4a48 100%)}
  .title-band{position:absolute;left:0;top:478px;width:515px;height:172px}
  .title{position:absolute;right:26px;top:486px;text-align:right;color:#fff}
  .title-top{font-family:"Montserrat",sans-serif;font-weight:600;font-size:27px;letter-spacing:.5px}
  .title-main{font-family:"Montserrat",sans-serif;font-weight:300;font-size:52px;line-height:1;letter-spacing:1px}
  .cta{position:absolute;left:0;top:650px;width:515px;height:48px}
  .cta-phone{position:absolute;left:18px;top:660px;display:flex;align-items:center;gap:8px;color:#fff;font-family:"Montserrat",sans-serif;font-weight:700;font-size:22px}
  .cta-web{position:absolute;right:22px;top:663px;color:#fff;font-family:"Montserrat",sans-serif;font-size:19px;font-weight:300}
  .cta-web b{font-weight:700}
</style>
</head>
<body>
<div class="spread">

  <section class="page page--back">
    <div class="top-band"></div>

    <div class="about">
      <h2 class="section-title">About us</h2>
      <div class="section-rule"></div>
      <p>RKS ltd (RKS) has the mission to solve any client's environmental problem with best process solution available on the market, most reliable and economical both on the CAPEX and OPEX.</p>
      <p>RKS want to optimize the client's benefits: energy, water recycle, products recovery and emission minimization.</p>
      <p>RKS verify any proposed process with its internal labs and pilot tests.</p>
    </div>

    <div class="block-blue block-blue--right"></div>
    <div class="block-blue block-blue--left"></div>
    <div class="photo photo--tank" role="img" aria-label="Photo of a circular clarifier tank filled with water"></div>
    <div class="photo photo--plant" role="img" aria-label="Photo of treatment plant basins with railings among trees"></div>

    <div class="contact">
      <h2 class="section-title">Get in touch</h2>
      <div class="section-rule"></div>
      <ul class="contact-list">
        <li>
          <svg width="14" height="14" viewBox="0 0 14 14"><path d="M7 1a4 4 0 0 0-4 4c0 3 4 7 4 7s4-4 4-7a4 4 0 0 0-4-4z" fill="none" stroke="#c2185b" stroke-width="1.6"/><circle cx="7" cy="5" r="1.4" fill="#c2185b"/></svg>
          <span>RKS Srl - Lindell Road</span>
        </li>
        <li class="indent">58/12 - Arvenna</li>
        <li>
          <svg width="14" height="14" viewBox="0 0 14 14"><path d="M2 5c0-2 2-3 5-3s5 1 5 3l-2 1-1-1H5L4 6zM3 7h8l1 5H2z" fill="#c2185b"/></svg>
          <span>011.5820947</span>
        </li>
        <li>
          <svg width="14" height="14" viewBox="0 0 14 14"><path d="M3 2l2 0 1 3-1.5 1a7 7 0 0 0 3.5 3.5L9 8l3 1v2a1 1 0 0 1-1 1A9 9 0 0 1 2 3a1 1 0 0 1 1-1z" fill="#c2185b"/></svg>
          <span>335 208 6413</span>
        </li>
        <li class="indent">VAT:10427739015</li>
      </ul>
    </div>

    <div class="social" aria-label="Social channels">
      <span></span><span></span><span></span><span></span><span></span><span></span>
    </div>
  </section>

  <section class="page page--front">
    <div class="front-accent"></div>
    <div class="brand">
      <span class="brand-mark"></span>
      <span class="brand-name">RKS<br>Rovalin Kestra Sulvane</span>
    </div>

    <div class="cover-photo" role="img" aria-label="Photo of large cylindrical biological oxidation tanks with walkways and railings"></div>

    <svg class="title-band" viewBox="0 0 515 172" preserveAspectRatio="none">
      <polygon points="0,70 515,0 515,172 0,172" fill="rgba(38,38,40,.9)"/>
    </svg>
    <div class="title">
      <div class="title-top">BIOLOGICAL OXIDATIVE</div>
      <div class="title-main">TREATMENT</div>
    </div>

    <svg class="cta" viewBox="0 0 515 48" preserveAspectRatio="none">
      <polygon points="0,0 250,0 235,48 0,48" fill="#e4541b"/>
      <polygon points="250,0 515,0 515,48 235,48" fill="#2f5f97"/>
    </svg>
    <div class="cta-phone">
      <svg width="20" height="20" viewBox="0 0 14 14"><path d="M3 2l2 0 1 3-1.5 1a7 7 0 0 0 3.5 3.5L9 8l3 1v2a1 1 0 0 1-1 1A9 9 0 0 1 2 3a1 1 0 0 1 1-1z" fill="#fff"/></svg>
      <span>335 208 6413</span>
    </div>
    <div class="cta-web">www.<b>rkssulvane</b>.com</div>
  </section>

</div>
</body>
</html>
```